Book cover for ebook and Physical book for Mind Clutter Collective

I run a non-profit Mind Clutter Collective and I have a new book that needs a cover. For the physical book, I will need a full wrap. The mission is to help individuals Quiet the cycle of restless worry patterns. This book is title is "Quiet the cycle of restless worry patterns", and subtitle "Clear Your Mind of Static Noise." I am open to anything design wise, nothing is set in stone. Oh, MCC is pending Trademark.

Target Market(s)

Typically it's Mom's from 25-40

Industry/Entity Type

Mental Health

Font styles to use
Serif

Colors
f37122
9bcb3b
fbed22
0255a3
e34197

Requirements
Must have
• I do like simplicity, yet vibrant colors.
Nice to have
• The authors are Rex T. Whitford, and Dana Okonkwo. For some inspiration individuals refer to me as the Wonder Guide having reversed five incurable diseases.
Should not have
• The cover shouldn't be too busy.

```html
<!DOCTYPE html>
<html lang="en">
<head>
<meta charset="utf-8">
<title>Quiet the Cycle of Restless Worry Patterns — Front Cover</title>
<link rel="stylesheet" href="https://fonts.googleapis.com/css2?family=Roboto+Slab:wght@700;800&family=Stint+Ultra+Condensed&display=swap">
<style>
  :root {
    --ink: #000000;
    --band-light: #fbed22;
    --band-mid: #f3d91a;
    --band-dark: #e2b80f;
    --title-yellow: #f2f21e;
    --title-yellow-deep: #d8d414;
    --author-cream: #f4f0b0;
    --rule-gold: #b8921e;
    --glow-white: #fffbe6;
    --glow-yellow: #f7e23a;
    --art-teal: #2bb3b0;
    --art-magenta: #b0368c;
    --art-red: #8e1e2a;
    --art-green: #3aa04a;
    --art-blue: #1b4f9a;
  }
  * { box-sizing: border-box; margin: 0; padding: 0; }
  html, body {
    width: 800px;
    height: 1200px;
    overflow: hidden;
    background: var(--ink);
  }
  .front-cover {
    position: relative;
    width: 800px;
    height: 1200px;
    background: var(--ink);
    overflow: hidden;
  }
  .tagline-band {
    position: absolute;
    top: 0; left: 0;
    width: 800px;
    height: 58px;
    background: linear-gradient(180deg, var(--band-light) 0%, var(--band-mid) 60%, var(--band-dark) 100%);
    display: flex;
    align-items: center;
    justify-content: center;
    z-index: 2;
  }
  .tagline {
    font-family: "Roboto Slab", serif;
    font-weight: 800;
    font-size: 26px;
    letter-spacing: 2px;
    color: var(--ink);
    text-transform: uppercase;
    white-space: nowrap;
  }
  .cover-art {
    position: absolute;
    top: 58px; left: 0;
    width: 800px;
    height: 560px;
    background:
      radial-gradient(ellipse 200px 190px at 400px 120px, var(--glow-white) 0%, var(--glow-yellow) 45%, rgba(247,226,58,0) 100%),
      radial-gradient(ellipse 240px 240px at 80px 150px, var(--art-red) 0%, rgba(142,30,42,0) 100%),
      radial-gradient(ellipse 260px 260px at 720px 170px, var(--art-teal) 0%, rgba(43,179,176,0) 100%),
      radial-gradient(ellipse 220px 180px at 640px 30px, var(--art-magenta) 0%, rgba(176,54,140,0) 100%),
      radial-gradient(ellipse 300px 200px at 130px 380px, var(--art-green) 0%, rgba(58,160,74,0) 100%),
      radial-gradient(ellipse 340px 200px at 560px 400px, var(--art-blue) 0%, rgba(27,79,154,0) 100%),
      linear-gradient(180deg, #6b5a2a 0%, #3a4a4a 55%, var(--ink) 100%);
  }
  .cover-art::after {
    content: "";
    position: absolute;
    left: 0; right: 0; bottom: 0;
    height: 180px;
    background: linear-gradient(180deg, rgba(0,0,0,0) 0%, var(--ink) 100%);
  }
  .title {
    font-family: "Stint Ultra Condensed", serif;
    font-weight: 400;
    color: var(--title-yellow);
    text-transform: uppercase;
  }
  .title-lead,
  .title-line {
    position: absolute;
    left: 0;
    width: 800px;
    text-align: center;
    white-space: nowrap;
    z-index: 2;
  }
  .title-lead {
    top: 606px;
    font-size: 172px;
    line-height: 160px;
    letter-spacing: 22px;
    text-indent: 22px;
    color: var(--title-yellow-deep);
  }
  .title-line {
    font-size: 100px;
    line-height: 100px;
    letter-spacing: 5px;
    text-indent: 5px;
  }
  .title-line--one { top: 752px; }
  .title-line--two { top: 852px; }
  .title-line--three { top: 952px; }
  .title-rule {
    position: absolute;
    top: 1056px;
    left: 158px;
    width: 484px;
    height: 2px;
    background: var(--rule-gold);
  }
  .authors {
    position: absolute;
    top: 1074px; left: 0;
    width: 800px;
    text-align: center;
    font-family: "Stint Ultra Condensed", serif;
    font-weight: 400;
    font-size: 56px;
    line-height: 60px;
    letter-spacing: 4px;
    text-indent: 4px;
    color: var(--author-cream);
    text-transform: uppercase;
    white-space: nowrap;
  }
</style>
</head>
<body>
  <main class="front-cover">
    <header class="tagline-band">
      <p class="tagline">Clear Your Mind of Static Noise</p>
    </header>

    <div class="cover-art" role="img" aria-label="Vibrant stained-glass mosaic illustration of a person holding their head, bursting into light and colourful fragments"></div>

    <h1 class="title">
      <span class="title-lead">Quiet</span>
      <span class="title-line title-line--one">The Cycle</span>
      <span class="title-line title-line--two">Of Restless</span>
      <span class="title-line title-line--three">Worry Patterns</span>
    </h1>

    <div class="title-rule"></div>

    <p class="authors">Rex T. Whitford and Dana Okonkwo</p>
  </main>
</body>
</html>
```